Business brochure for a human resources company

I am looking for a commercial brochure for my company which is based on payroll management and human resources.
I wish it had the same colors and design as the logo, Gold and Black.
I would like to highlight the services of my company.
The brochure should show the quality, professionalism and modernity of the company.
The company has two poles, a legal and a social
A place must show the company logo
The target audience is accounting firms as well as small and medium enterprises.
Small and Medium Enterprise, Accounting firm
Paie et Ressources humaines

```html
<!DOCTYPE html>
<html lang="en">
<head>
<meta charset="utf-8">
<title>Valoris – HR &amp; Payroll Brochure</title>
<link href="https://fonts.googleapis.com/css2?family=Montserrat:wght@400;600;700;800;900&family=Open+Sans:wght@400;600&display=swap" rel="stylesheet">
<style>
  :root{
    --bg:#e4e4e4;
    --black:#0d0d0d;
    --ink:#1a1a1a;
    --gold:#c9a24a;
    --gold-light:#f0d488;
    --gold-dark:#8e6a22;
    --white:#ffffff;
    --grey-text:#6d6d6d;
    --soft-text:#bdbdbd;
  }
  *{box-sizing:border-box;margin:0;padding:0}
  html,body{width:1200px;height:4000px;overflow:hidden}
  body{background:var(--bg);font-family:"Open Sans",Arial,sans-serif;position:relative}
  .spread{position:absolute;left:50px;width:1100px;height:760px;overflow:hidden;box-shadow:0 8px 30px rgba(0,0,0,.18)}
  .spread--cover{top:990px;background:var(--black)}
  .spread--inside{top:2250px;background:var(--white)}
  .spread__art{position:absolute;inset:0;width:1100px;height:760px}
  .brand{position:absolute;display:flex;align-items:center;gap:8px;font-family:"Montserrat",Arial,sans-serif;font-weight:800;color:var(--gold);letter-spacing:2px}
  .brand__mark{width:14px;height:14px;background:var(--gold)}
  .brand--front{left:780px;top:40px;font-size:28px}
  .brand--back{left:60px;top:628px;font-size:22px}

  .about{position:absolute;left:110px;top:190px;width:330px;height:180px;border:2px solid var(--gold);border-radius:6px;background:#111;padding:18px 22px}
  .about__title{font-family:"Montserrat",Arial,sans-serif;font-weight:700;font-size:14px;color:var(--white);text-align:center;letter-spacing:1px;margin-bottom:12px}
  .about__text{font-size:10.5px;line-height:1.6;color:var(--soft-text);text-align:center}

  .contact{position:absolute;left:250px;top:612px;list-style:none;font-size:10px;color:var(--soft-text)}
  .contact li{display:flex;align-items:center;gap:8px;margin-bottom:8px}
  .contact svg{width:12px;height:12px;fill:var(--gold)}

  .cover-title{position:absolute;left:550px;width:550px;text-align:center;font-family:"Montserrat",Arial,sans-serif;color:var(--white)}
  .cover-title__main{top:500px;font-size:54px;font-weight:900;letter-spacing:1px}
  .cover-title__sub{top:568px;font-size:27px;font-weight:700}
  .ribbon{position:absolute;left:655px;top:618px;width:340px;height:34px;background:linear-gradient(90deg,var(--gold-dark),var(--gold-light),var(--gold));display:flex;align-items:center;justify-content:center;font-family:"Montserrat",Arial,sans-serif;font-size:12px;font-weight:700;color:var(--ink)}

  .services{position:absolute;left:40px;top:45px;width:230px}
  .services__title{font-family:"Montserrat",Arial,sans-serif;font-weight:800;font-size:22px;color:var(--white);margin-bottom:14px}
  .services__text{font-size:10px;line-height:1.65;color:var(--soft-text)}
  .gold-panel{position:absolute;left:300px;top:100px;width:215px;padding:20px 18px;color:var(--ink)}
  .gold-panel__title{font-family:"Montserrat",Arial,sans-serif;font-weight:700;font-size:14px;margin-bottom:8px}
  .gold-panel__text{font-size:10px;line-height:1.6}

  .values{position:absolute;left:640px;top:320px;width:420px;list-style:none}
  .value{display:flex;gap:18px;margin-bottom:36px}
  .value__icon{flex:0 0 46px;height:46px}
  .value__name{font-family:"Montserrat",Arial,sans-serif;font-weight:700;font-size:17px;color:var(--gold-dark);margin-bottom:6px}
  .value__text{font-size:10px;line-height:1.6;color:var(--grey-text)}
</style>
</head>
<body>

<section class="spread spread--cover">
  <svg class="spread__art" viewBox="0 0 1100 760">
    <defs>
      <radialGradient id="hrPhoto" cx="50%" cy="45%" r="60%">
        <stop offset="0" stop-color="#9fe3ff"/>
        <stop offset=".5" stop-color="#3f9fd8"/>
        <stop offset="1" stop-color="#0b3d66"/>
      </radialGradient>
      <linearGradient id="goldRing" x1="0" y1="0" x2="1" y2="1">
        <stop offset="0" stop-color="#f0d488"/>
        <stop offset=".5" stop-color="#c9a24a"/>
        <stop offset="1" stop-color="#8e6a22"/>
      </linearGradient>
      <linearGradient id="frontShade" x1="0" y1="0" x2="0" y2="1">
        <stop offset="0" stop-color="#1b1b1b"/>
        <stop offset="1" stop-color="#050505"/>
      </linearGradient>
    </defs>
    <rect x="550" y="0" width="550" height="760" fill="url(#frontShade)"/>
    <line x1="550" y1="0" x2="550" y2="760" stroke="#222" stroke-width="1"/>
    <circle cx="825" cy="290" r="176" fill="none" stroke="url(#goldRing)" stroke-width="12"/>
    <circle cx="825" cy="290" r="160" fill="url(#hrPhoto)" role="img" aria-label="Photo: hand touching a glowing human resources network interface"/>
    <path d="M660 400 A180 180 0 0 0 990 140" fill="none" stroke="url(#goldRing)" stroke-width="8"/>
    <polygon points="1006,118 978,134 998,152" fill="#e0bd66"/>
  </svg>

  <div class="about">
    <h2 class="about__title">ABOUT US</h2>
    <p class="about__text">We support small and medium enterprises and accounting firms with reliable payroll management and human resources advice. Our legal and social teams work side by side to deliver clear, compliant and modern solutions adapted to every client.</p>
  </div>

  <div class="brand brand--back"><span class="brand__mark"></span>VALORIS</div>
  <ul class="contact">
    <li><svg viewBox="0 0 24 24"><path d="M6.6 10.8a15 15 0 0 0 6.6 6.6l2.2-2.2c.3-.3.7-.4 1-.2 1.1.4 2.3.6 3.6.6.6 0 1 .4 1 1V20c0 .6-.4 1-1 1A17 17 0 0 1 3 4c0-.6.4-1 1-1h3.5c.6 0 1 .4 1 1 0 1.3.2 2.5.6 3.6.1.3 0 .7-.2 1z"/></svg>+1 (555) 010-2040</li>
    <li><svg viewBox="0 0 24 24"><path d="M12 2a7 7 0 0 0-7 7c0 5 7 13 7 13s7-8 7-13a7 7 0 0 0-7-7zm0 9.5A2.5 2.5 0 1 1 12 6.5a2.5 2.5 0 0 1 0 5z"/></svg>12 Harbor Lane, Springfield</li>
    <li><svg viewBox="0 0 24 24"><path d="M2 5h20v14H2zm2 2v.5l8 5 8-5V7l-8 5z"/></svg>hello@valorisrh.example</li>
  </ul>

  <div class="brand brand--front"><span class="brand__mark"></span>VALORIS</div>
  <h1 class="cover-title cover-title__main">LOREM IPSUM</h1>
  <p class="cover-title cover-title__sub">IS SIMPLY DUMMY TEXT</p>
  <div class="ribbon">www.valorisrh.example</div>
</section>

<section class="spread spread--inside">
  <svg class="spread__art" viewBox="0 0 1100 760">
    <defs>
      <linearGradient id="goldPanel" x1="0" y1="0" x2="1" y2="1">
        <stop offset="0" stop-color="#f0d488"/>
        <stop offset=".55" stop-color="#c9a24a"/>
        <stop offset="1" stop-color="#9a7428"/>
      </linearGradient>
      <linearGradient id="cityFade" x1="0" y1="0" x2="0" y2="1">
        <stop offset="0" stop-color="#ffffff" stop-opacity="0"/>
        <stop offset=".5" stop-color="#d9c8a8" stop-opacity=".7"/>
        <stop offset="1" stop-color="#a8927a"/>
      </linearGradient>
      <linearGradient id="deskFade" x1="1" y1="0" x2="0" y2="1">
        <stop offset="0" stop-color="#9aa3ad"/>
        <stop offset=".55" stop-color="#d6dadf"/>
        <stop offset="1" stop-color="#ffffff" stop-opacity="0"/>
      </linearGradient>
      <linearGradient id="meetPhoto" x1="0" y1="0" x2="1" y2="1">
        <stop offset="0" stop-color="#c9b79a"/>
        <stop offset="1" stop-color="#5e5548"/>
      </linearGradient>
    </defs>
    <rect x="660" y="0" width="440" height="280" fill="url(#deskFade)" role="img" aria-label="Photo: hands reviewing charts and reports on a desk"/>
    <rect x="0" y="0" width="400" height="760" fill="#0d0d0d"/>
    <circle cx="300" cy="340" r="296" fill="#0d0d0d"/>
    <path d="M349.5 59 A285 285 0 1 1 202.5 608" fill="none" stroke="url(#goldPanel)" stroke-width="22"/>
    <rect x="0" y="580" width="1100" height="180" fill="url(#cityFade)" role="img" aria-label="Photo: city skyline with business people, fading into the page"/>
    <rect x="300" y="100" width="215" height="190" fill="url(#goldPanel)"/>
    <circle cx="95" cy="510" r="78" fill="url(#goldPanel)"/>
    <circle cx="95" cy="510" r="70" fill="url(#meetPhoto)" role="img" aria-label="Photo: business handshake"/>
    <circle cx="250" cy="540" r="78" fill="url(#goldPanel)"/>
    <circle cx="250" cy="540" r="70" fill="#7d8fa1" role="img" aria-label="Photo: team of colleagues in a meeting"/>
  </svg>

  <div class="services">
    <h2 class="services__title">OUR SERVICES</h2>
    <p class="services__text">From payslips to contracts, we handle every step of payroll and staff administration. Our legal pole secures your obligations while our social pole guides your teams, so you can focus on growing your business.</p>
  </div>
  <div class="gold-panel">
    <h3 class="gold-panel__title">Lorem Ipsum</h3>
    <p class="gold-panel__text">Tailored support for accounting firms and growing companies, with dedicated experts, clear reporting and fast answers to every question.</p>
  </div>

  <ul class="values">
    <li class="value">
      <svg class="value__icon" viewBox="0 0 46 46"><circle cx="23" cy="23" r="22" fill="#c9a24a"/><polygon points="23,9 27,19 38,19 29,26 32,37 23,30 14,37 17,26 8,19 19,19" fill="#fff"/></svg>
      <div><h3 class="value__name">Quality</h3><p class="value__text">Accurate payroll and careful follow-up for each file, checked by experienced specialists at every stage.</p></div>
    </li>
    <li class="value">
      <svg class="value__icon" viewBox="0 0 46 46"><circle cx="23" cy="23" r="22" fill="#c9a24a"/><circle cx="23" cy="16" r="6" fill="#fff"/><path d="M12 34a11 9 0 0 1 22 0z" fill="#fff"/></svg>
      <div><h3 class="value__name">Professionalism</h3><p class="value__text">A committed team that respects deadlines, confidentiality and the rules that govern your sector.</p></div>
    </li>
    <li class="value">
      <svg class="value__icon" viewBox="0 0 46 46"><circle cx="23" cy="23" r="22" fill="#c9a24a"/><rect x="12" y="26" width="5" height="9" fill="#fff"/><rect x="20" y="20" width="5" height="15" fill="#fff"/><rect x="28" y="13" width="5" height="22" fill="#fff"/></svg>
      <div><h3 class="value__name">Modernity</h3><p class="value__text">Digital tools and online access that make managing your people simple, fast and transparent.</p></div>
    </li>
  </ul>
</section>

</body>
</html>
```